Fairway Battery Program Email marketing campaign for Corvel Energy

Design a visually engaging and professional marketing email to promote the upcoming Federal Government Battery Subsidy to our existing solar clients, encouraging them to install a battery system now to maximise savings. email content example "Subject: ⚡ Federal Government Battery Subsidy is Coming – Maximise Your Solar Savings

Body:
Hi [First Name],

Great news! With the federal election now decided, the Federal Government’s Home Battery Subsidy Program is officially on the way.

While the scheme hasn’t formally launched yet, it's guaranteed—and like the solar rebate before it, the subsidy reduces each year, so the earlier you install, the more you’ll save.

Crucially, the subsidy is only available once per household, so it makes sense to install a system that fully meets your home's battery needs right from the start.

Why add a battery to your existing solar system now?
✅ Store your excess solar energy instead of sending it back to the grid for low feed-in tariffs
✅ Use your stored solar power at night, when electricity prices are highest (typically 5–8pm)
✅ Slash your power bills and avoid rising time-of-use charges
✅ Protect your home from power outages
✅ Increase your self-sufficiency and long-term energy security

If you’ve already installed solar with us, now is the ideal time to complete your setup with a battery system designed to maximise your return—and take full advantage of this one-off federal subsidy.

Call us today or reply to this email to secure your spot and beat the rush.

Let your solar work smarter for your home,
The Corvel Energy Team"

Content: We’ve provided the copy (see attached or below). The key points to emphasise in the design are: The urgency (subsidy winds down each year, limited to one per household). The benefits of installing a battery now, including energy savings, time-of-use charge avoidance, and self-sufficiency. Call to action: “Call us today or reply to this email to secure your spot and beat the rush.”

Industry/Entity Type

Renewable Energy

Colors
0054AA
0677BA
7BADD7
CADEEF
E8F1F8
EB3D1F
EC4F4E
F09395
F8D3D4
FCEDEE

Requirements
Must have
• Clean, modern, and trustworthy – aligned with Corvel Energy branding. Bold headers and icons to make key points stand out. Include visual elements such as: A solar battery image Infographic or icon-style section showing key battery benefits (e.g. bill savings, backup power, self-consumption) Highlighted call-to-action button (“Secure My Battery Now” or “Beat the Rush”)
Nice to have
• I would like to have our company imagery (Corvel Energy) alongside the battery brands we offer being Pelto, KVM, Tarmilo and Norvique
Should not have
• Unsure

```html
<!DOCTYPE html>
<html lang="en">
<head>
<meta charset="utf-8">
<title>Corvel Energy – Fairway Battery Program Email</title>
<link href="https://fonts.googleapis.com/css2?family=Open+Sans:wght@300;400;600;700&family=Nunito+Sans:wght@300;400;600;700;800&display=swap" rel="stylesheet">
<style>
:root{
  --stage:#5e5e5e;
  --red:#c01f2f;
  --red-deep:#8e0f1a;
  --navy:#2f3547;
  --slate:#3d4352;
  --ink:#2b2b2b;
  --white:#ffffff;
  --mist:#d3d5d9;
}
*{box-sizing:border-box;margin:0;padding:0}
html,body{width:709px;height:1200px;overflow:hidden;background:var(--stage)}
body{font-family:"Nunito Sans",sans-serif;color:var(--ink);font-weight:300}
.email{position:absolute;left:201px;top:36px;width:307px;height:1128px;background:var(--white);overflow:hidden}
.abs{position:absolute}

/* header */
.header{left:0;top:0;width:307px;height:66px;background:var(--white)}
.brand{left:22px;top:26px;display:flex;align-items:center;gap:4px}
.brand-square{width:11px;height:11px;background:var(--red)}
.brand-name{font-family:"Nunito Sans",sans-serif;font-weight:800;font-size:11px;line-height:10px;color:var(--navy);letter-spacing:.3px}
.social{width:7px;height:7px;border-radius:50%;background:var(--white)}

/* hero */
.hero{left:0;top:65.5px;width:307px;height:162px}
.hero-photo{left:0;top:0;width:307px;height:162px;background:linear-gradient(160deg,#6b6a63 0%,#c9a063 30%,#f1d58f 42%,#6f7f95 65%,#2a3850 100%)}
.hero-title{right:22px;top:21px;width:130px;text-align:right;font-family:"Open Sans",sans-serif;font-weight:400;font-size:12px;line-height:14.4px;color:var(--white)}
.hero-btn{left:167px;top:112px;width:118px;height:29px;border:1.5px solid var(--white);background:linear-gradient(90deg,#b0101d,#d01827);color:var(--white);font-family:"Open Sans",sans-serif;font-weight:700;font-size:9.5px;display:flex;align-items:center;justify-content:center;letter-spacing:.2px}

/* intro */
.intro-art{left:59px;top:243px;width:186px;height:108px;background:radial-gradient(ellipse at 30% 40%,#3a7ad8 0 14%,transparent 15%),radial-gradient(ellipse at 75% 35%,#f2b86a 0 16%,transparent 17%),linear-gradient(180deg,#ffffff 0%,#eceef1 70%,#ffffff 100%)}
.greeting{left:0;top:366px;width:307px;text-align:center;font-family:"Open Sans",sans-serif;font-size:10.5px;color:var(--red)}
.copy{left:28px;width:251px;text-align:center;font-size:6.6px;line-height:9px;color:var(--ink);font-weight:300}

/* benefits */
.benefits{left:0;top:485.5px;width:307px;height:185.5px;background:linear-gradient(180deg,var(--slate) 0%,#444a58 40%,#2e3340 100%)}
.benefits-title{left:0;top:18px;width:307px;text-align:center;font-family:"Open Sans",sans-serif;font-weight:300;font-size:10.2px;color:var(--white)}
.card{top:47px;width:47.3px;height:118px;background:var(--red);border-radius:1.5px;text-align:center;color:var(--white)}
.card::before{content:"";position:absolute;left:19px;top:-3px;width:9px;height:3px;background:var(--red);border-radius:1px 1px 0 0}
.card svg{display:block;margin:7px auto 0;width:22px;height:22px}
.card p{font-size:7px;line-height:8.3px;margin-top:5px;padding:0 2px;font-weight:300}

/* closing */
.closing{left:28px;top:689px;width:251px;text-align:center;font-size:6.6px;line-height:9px;font-weight:300}
.cta-band{left:0;top:732px;width:307px;height:33px;background:var(--navy)}
.cta-box{left:113px;top:723.5px;width:80px;height:17px;background:var(--red);border:1.2px solid var(--white);color:var(--white);font-family:"Open Sans",sans-serif;font-weight:700;font-size:10.5px;display:flex;align-items:center;justify-content:center}
.cta-sub{left:0;top:745px;width:307px;text-align:center;font-size:6.6px;line-height:9px;color:var(--white);font-weight:300}
.cta-sub strong{font-weight:700}
.signoff{left:0;top:775px;width:307px;text-align:center;font-size:6.6px;line-height:9px;font-weight:300}
.signoff strong{color:var(--red);font-weight:700}
.mark{left:0;top:821px;width:307px;display:flex;justify-content:center;align-items:center;gap:4px}
.mark .brand-square{width:10px;height:10px}
.mark span{font-weight:800;font-size:9px;color:var(--navy)}

/* partners */
.partner-band{left:0;top:953.5px;width:307px;height:53.5px;background:var(--red)}
.unit{background:linear-gradient(90deg,#dcdcdc,#f7f7f7 40%,#e6e6e6)}
.unit.dark{background:linear-gradient(90deg,#4a4c50,#7a7c80 50%,#55575b)}
.unit.split{background:linear-gradient(90deg,#3b3d41 0 14%,#f5f5f5 14%,#ffffff 100%)}
.partner-name{top:984px;width:70px;text-align:center;font-weight:700;font-size:7px;letter-spacing:.8px;color:var(--white)}

/* footer */
.footer{left:0;top:1004px;width:307px;height:102.5px;background:var(--navy);color:var(--white)}
.footer .brand{left:0;top:22px;width:307px;justify-content:center}
.footer .brand-name{color:var(--white)}
.footer-contact{left:0;top:59px;width:307px;text-align:center;font-size:4.3px;font-weight:400}
.legal{left:0;top:1106.5px;width:307px;height:21.5px;background:var(--mist);font-size:4.3px;color:#555;display:flex;align-items:center;justify-content:center;font-weight:400}
.legal u{text-decoration:underline}
</style>
</head>
<body>
<main class="email">

  <header class="header abs">
    <svg class="abs" style="left:0;top:0" width="307" height="66" aria-hidden="true"><polygon points="107,0 307,0 307,66 143.6,66" fill="var(--red)"/></svg>
    <div class="brand abs"><span class="brand-square"></span><span class="brand-name">CORVEL<br>ENERGY</span></div>
    <span class="social abs" style="left:193.5px;top:32.5px" aria-label="Social link"></span>
    <span class="social abs" style="left:213.5px;top:32.5px" aria-label="Social link"></span>
    <span class="social abs" style="left:235.5px;top:32.5px" aria-label="Social link"></span>
    <span class="social abs" style="left:257.5px;top:32.5px" aria-label="Social link"></span>
    <span class="social abs" style="left:277.5px;top:32.5px" aria-label="Social link"></span>
  </header>

  <section class="hero abs">
    <div class="hero-photo abs" role="img" aria-label="Rows of solar panels glowing under a golden sunset sky"></div>
    <svg class="abs" style="left:0;top:0" width="307" height="162" aria-hidden="true">
      <defs><linearGradient id="heroRed" x1="0" y1="0" x2="0.4" y2="1"><stop offset="0" stop-color="#c01f2f"/><stop offset="0.6" stop-color="#a3121f"/><stop offset="1" stop-color="#6e0a14"/></linearGradient></defs>
      <polygon points="143.6,0 307,0 307,162 234,162" fill="url(#heroRed)"/>
    </svg>
    <h1 class="hero-title abs" style="font-weight:400">Federal Government<br>Battery Subsidy is<br>Coming –<br>Maximise Your<br>Solar Savings</h1>
    <div class="hero-btn abs">KNOW MORE</div>
  </section>

  <div class="intro-art abs" role="img" aria-label="Solar panel and gold dollar sign balanced on a seesaw"></div>
  <p class="greeting abs">Hi [First Name],</p>
  <p class="copy abs" style="top:392px">Great news! With the federal election now decided, the Federal Government’s Home Battery Subsidy Program is officially on the way.</p>
  <p class="copy abs" style="top:419px">While the scheme hasn’t formally launched yet, it's guaranteed—and like the solar rebate before it, the subsidy reduces each year, so the earlier you install, the more you’ll save.</p>
  <p class="copy abs" style="top:455px">Crucially, the subsidy is only available once per household, so it makes sense to install a system that fully meets your home's battery needs right from the start.</p>

  <section class="benefits abs">
    <h2 class="benefits-title abs">Why add a battery to your existing solar system now?</h2>
    <div class="card abs" style="left:21.5px">
      <svg viewBox="0 0 24 24" aria-hidden="true"><rect x="2" y="6" width="20" height="15" fill="#fff"/><rect x="5" y="4" width="3" height="2" fill="#fff"/><rect x="16" y="4" width="3" height="2" fill="#fff"/><path d="M6 13h3M16 13h3M17.5 11.5v3M12.5 10l-2 4h3l-2 4" stroke="#c01f2f" stroke-width="1.2" fill="none"/></svg>
      <p>Store your excess solar energy instead of sending it back to the grid for low feed-in tariffs</p>
    </div>
    <div class="card abs" style="left:75.5px">
      <svg viewBox="0 0 24 24" aria-hidden="true"><path d="M14 2a10 10 0 1 0 8 14A8 8 0 0 1 14 2z" fill="#fff"/><path d="M13 9l-3 5h3l-2 5" stroke="#c01f2f" stroke-width="1.4" fill="none"/></svg>
      <p>Use your stored solar power at night, when electricity prices are highest (typically 5–8pm)</p>
    </div>
    <div class="card abs" style="left:129.5px">
      <svg viewBox="0 0 24 24" aria-hidden="true"><rect x="3" y="2" width="14" height="19" rx="1" fill="#fff"/><path d="M11 4l-3 5h3l-2 5" stroke="#c01f2f" stroke-width="1.4" fill="none"/><circle cx="18" cy="17" r="4.5" fill="#fff" stroke="#c01f2f" stroke-width="1"/><path d="M18 15v4M16.5 17.5l1.5 1.5 1.5-1.5" stroke="#c01f2f" stroke-width="1" fill="none"/></svg>
      <p>Slash your power bills and avoid rising time-of-use charges</p>
    </div>
    <div class="card abs" style="left:183.5px">
      <svg viewBox="0 0 24 24" aria-hidden="true"><path d="M12 2L2 11h3v11h14V11h3z" fill="#fff"/><path d="M12 9l5 2v4c0 3-2.5 4.5-5 5.5-2.5-1-5-2.5-5-5.5v-4z" fill="#c01f2f"/><path d="M12.5 11l-2 3.5h2l-1 3" stroke="#fff" stroke-width="1" fill="none"/></svg>
      <p>Protect your home from power outages</p>
    </div>
    <div class="card abs" style="left:237.5px">
      <svg viewBox="0 0 24 24" aria-hidden="true"><rect x="10" y="12" width="3" height="5" fill="#fff"/><rect x="14" y="9" width="3" height="8" fill="#fff"/><rect x="18" y="5" width="3" height="12" fill="#fff"/><path d="M2 19c4-2 7-2 10 0l7-3v3l-7 4-10-2z" fill="#fff"/><path d="M7 2l3 1v3c0 2-1.5 3-3 3.5C5.5 9 4 8 4 6V3z" fill="#fff"/></svg>
      <p>Increase your self-sufficiency and long-term energy security</p>
    </div>
  </section>

  <p class="closing abs">If you’ve already installed solar with us, now is the ideal time to complete your setup with a battery system designed to maximise your return—and take full advantage of this one-off federal subsidy.</p>
  <div class="cta-band abs"></div>
  <div class="cta-box abs">Call us Today</div>
  <p class="cta-sub abs">or reply to this email to secure your spot and<br><strong>Beat the Rush.</strong></p>
  <p class="signoff abs">Let your solar work smarter for your home,<br><strong>The Corvel Energy Team</strong></p>
  <div class="mark abs"><span class="brand-square"></span><span>CORVEL</span></div>

  <div class="partner-band abs"></div>
  <div class="unit abs" style="left:20px;top:887px;width:54px;height:89px" role="img" aria-label="KVM stacked home battery unit"></div>
  <div class="unit dark abs" style="left:90px;top:870px;width:49px;height:106px" role="img" aria-label="Pelto home battery unit"></div>
  <div class="unit abs" style="left:157px;top:889px;width:59px;height:87px" role="img" aria-label="Tarmilo modular battery unit"></div>
  <div class="unit split abs" style="left:232px;top:877px;width:55px;height:99px" role="img" aria-label="Norvique home battery cabinet"></div>
  <div class="partner-name abs" style="left:12px">KVM</div>
  <div class="partner-name abs" style="left:79px">PELTO</div>
  <div class="partner-name abs" style="left:151px">TARMILO</div>
  <div class="partner-name abs" style="left:230px">NORVIQUE</div>

  <footer class="footer abs">
    <div class="brand abs"><span class="brand-square"></span><span class="brand-name">CORVEL<br>ENERGY</span></div>
    <div class="footer-contact abs">07 3000 0147 &nbsp;|&nbsp; 12/40 Harlow Street, Kelmont QLD 4120</div>
    <span class="social abs" style="left:106.5px;top:75.5px" aria-label="Social link"></span>
    <span class="social abs" style="left:126.5px;top:75.5px" aria-label="Social link"></span>
    <span class="social abs" style="left:148.5px;top:75.5px" aria-label="Social link"></span>
    <span class="social abs" style="left:170.5px;top:75.5px" aria-label="Social link"></span>
    <span class="social abs" style="left:190.5px;top:75.5px" aria-label="Social link"></span>
  </footer>
  <div class="legal abs">You're receiving this email because you subscribed to it.&nbsp;<u>Unsubscribe</u>, if you want to opt out!</div>

</main>
</body>
</html>
```